Geschäftspapiere
Zielgruppe
Valtoria is a Full Service Accounting and Consulting Company. It's appearance is young and fresh, yet professional and reliable.
Aufgabenstellung
We are looking for a design for consulting reports the company is compiling. The design should be delivered as Word-Template (.dot file) and should include:
* A decent cover page
* Heading format for 3 different levels
* Title format
* The 'content' page layout including a header and/or footer just as you think it's good looking
* If possible, it should also include a nice 'table of contents'
The template should be suitable for DIN A4 Paper and it will be printed on an usual, professional office printer.

```html
<!DOCTYPE html>
<html lang="en">
<head>
<meta charset="utf-8">
<title>Valtoria – Business Stationery</title>
<link rel="stylesheet" href="https://fonts.googleapis.com/css2?family=Oswald:wght@400&family=Catamaran:wght@400;600;700;800&family=Roboto:wght@400;500&display=swap">
<style>
:root{
  --board:#4a4a4c;
  --navy:#005085;
  --sky:#2b8fc9;
  --green:#7dc24b;
  --grey:#6b7072;
  --ink:#3a3a3a;
  --paper:#ffffff;
  --window:#dadfda;
}
*{margin:0;padding:0;box-sizing:border-box}
html,body{width:691px;height:1200px;overflow:hidden;background:var(--board)}
body{position:relative;font-family:"Catamaran",sans-serif;color:var(--ink)}
.sheet{position:absolute;background:var(--paper);overflow:hidden}
.abs{position:absolute}
.wordmark{font-family:"Catamaran",sans-serif;font-weight:800;color:var(--navy);letter-spacing:.02em;line-height:1;white-space:nowrap}
.brand{display:flex;align-items:center;gap:3px}
.mark-square{display:block;background:var(--green);flex:none}
.tagline{font-family:"Catamaran",sans-serif;color:var(--navy);letter-spacing:.12em;line-height:1;white-space:nowrap}

/* cover */
.cover{left:48px;top:77px;width:269px;height:380px}
.cover .wordmark{left:25px;top:34px;font-size:26px}
.report-title{left:26px;top:75px;font-family:"Oswald",sans-serif;color:var(--grey);font-size:13.5px;line-height:16px}
.cover-photo{left:0;top:135px;width:269px;height:245px;background:linear-gradient(160deg,#1d5f93 0%,#0b5488 45%,#2d6a8f 100%)}
.cover-address{left:25px;top:318px;color:#fff;font-size:6px;line-height:7px}
.cover-address .small{font-size:4.2px;line-height:5px;margin-top:1px}

/* back cover */
.back-cover{left:376px;top:77px;width:269px;height:380px;background:var(--navy)}
.back-cover .wordmark{width:100%;text-align:center;top:175px;font-size:19px;color:#fff}
.back-cover .tagline{width:100%;text-align:center;top:199px;font-size:6.8px;color:#d8e6f0}
.back-url{width:100%;text-align:center;top:343px;font-size:9px;color:var(--sky);font-weight:600}
.back-url b{color:#fff;font-weight:700}

/* contents */
.contents{left:48px;top:495px;width:269px;height:380px;font-family:"Roboto",sans-serif}
.contents-title{left:24px;top:270px;transform:rotate(-90deg);transform-origin:left top;font-family:"Roboto",sans-serif;font-weight:500;font-size:35px;color:var(--navy);letter-spacing:.02em;line-height:1}
.toc-section{left:68px;width:165px}
.toc-heading{font-size:9.3px;color:var(--navy);line-height:10.6px;margin-bottom:2px}
.toc-item{display:flex;justify-content:space-between;font-size:5.8px;color:var(--ink);line-height:8px}
.toc-item span:last-child{font-weight:500}

/* letterhead */
.letter{left:376px;top:495px;width:269px;height:380px}
.letter .brand{left:25px;top:48px}
.letter .wordmark{font-size:10px}
.letter .tagline{left:25px;top:61px;font-size:3.8px}
.letter-sender{left:25px;top:70px;font-size:2.6px;color:var(--ink);white-space:nowrap}
.letter-body{left:25px;top:129px;width:218px;font-family:"Roboto",sans-serif;font-size:3.5px;line-height:5.4px;text-align:justify;color:var(--ink)}
.letter-body p{margin-bottom:5px}
.signature{left:25px;top:218px;width:36px;height:16px;background:#eef1f3;border-radius:3px}
.letter-footer{top:347px;font-size:3.4px;line-height:4px;color:var(--grey);white-space:nowrap}
.footer-rule{top:347px;width:.5px;height:18px;background:var(--grey)}

/* envelopes */
.envelope-front{left:42px;top:981px;width:281px;height:141px}
.envelope-front .brand{left:26px;top:38px}
.envelope-front .wordmark{font-size:9.5px}
.envelope-front .tagline{left:26px;top:50px;font-size:3.6px}
.address-window{left:26px;top:65px;width:115px;height:57px;background:var(--window);border-radius:4px}
.envelope-back{left:368px;top:981px;width:281px;height:141px}

/* cards */
.card-front{left:370px;top:897px;width:109px;height:64px}
.card-front .brand{right:7px;top:15px}
.card-front .wordmark{font-size:5.5px}
.card-front .tagline{right:7px;top:22px;font-size:1.8px}
.card-name{left:6px;top:26px;font-size:4px;color:var(--ink);line-height:4px}
.card-role{left:6px;top:30.5px;font-size:2.6px;color:var(--grey);line-height:3px}
.card-rule{left:6px;top:34px;width:97px;height:.5px;background:var(--navy)}
.card-contact{left:6px;top:45px;font-size:2.5px;line-height:3.4px;color:var(--ink);white-space:nowrap}
.card-place{right:6px;top:52px;font-size:2.5px;line-height:3.4px;text-align:right;color:var(--ink);white-space:nowrap}
.card-back{left:537px;top:897px;width:109px;height:64px;background:var(--navy)}
.card-back .wordmark{width:100%;text-align:center;top:24px;font-size:10px;color:#fff}
.card-back-url{width:100%;text-align:center;top:52px;font-size:3.8px;color:#fff}
.url-tab{color:#fff;font-weight:600;text-align:center}
</style>
</head>
<body>

<!-- Cover -->
<section class="sheet cover">
  <div class="abs wordmark">valtoria</div>
  <div class="abs report-title">2022<br>ANNUAL REPORT</div>
  <svg class="abs" style="left:0;top:126px" width="269" height="8" viewBox="0 0 269 8">
    <polygon points="0,0 194,0 191,6 0,6" fill="var(--green)"/>
    <polygon points="197,0 269,0 269,6 194,6" fill="var(--navy)"/>
  </svg>
  <div class="abs cover-photo" role="img" aria-label="Photo of a smiling businessman in a suit on the phone under a glass roof, tinted blue"></div>
  <div class="abs cover-address">
    valtoria GmbH Lindhof<br>Ahornweg 14<br>52180 Feldstadt
    <div class="small">Phone&nbsp;&nbsp;: +49 555 / 010 200<br>Fax&nbsp;&nbsp;&nbsp;&nbsp;&nbsp;&nbsp;&nbsp;: +49 555 / 010 209<br>Mail&nbsp;&nbsp;&nbsp;&nbsp;&nbsp;: info@valtoria.de</div>
  </div>
</section>

<!-- Back cover -->
<section class="sheet back-cover">
  <div class="abs wordmark">valtoria</div>
  <div class="abs tagline">MARKETING &amp; CONSULTING</div>
  <div class="abs back-url">www.<b>valtoria</b>.de</div>
</section>

<!-- Contents -->
<section class="sheet contents">
  <div class="abs contents-title">CONTENT</div>
  <div class="abs toc-section" style="top:51px">
    <div class="toc-heading">Welcome</div>
    <div class="toc-item"><span>01 Lorem Ipsum</span><span>1</span></div>
    <div class="toc-item"><span>02 Lorem Ipsum</span><span>2</span></div>
  </div>
  <div class="abs toc-section" style="top:90px">
    <div class="toc-heading">This Year`s B2B Content Marketing Performance</div>
    <div class="toc-item"><span>01 Lorem Ipsum</span><span>5</span></div>
    <div class="toc-item"><span>02 Lorem Ipsum</span><span>7</span></div>
  </div>
  <div class="abs toc-section" style="top:140px">
    <div class="toc-heading">Usage &amp; Team Organization</div>
    <div class="toc-item"><span>01 Lorem Ipsum</span><span>9</span></div>
    <div class="toc-item"><span>02 Lorem Ipsum</span><span>10</span></div>
  </div>
  <div class="abs toc-section" style="top:180px">
    <div class="toc-heading">Commitment &amp; Overall Success</div>
    <div class="toc-item"><span>01 Lorem Ipsum</span><span>11</span></div>
    <div class="toc-item"><span>02 Lorem Ipsum</span><span>12</span></div>
  </div>
  <div class="abs toc-section" style="top:221px">
    <div class="toc-heading">Content Marketing Strategy</div>
    <div class="toc-item"><span>01 Lorem Ipsum</span><span>13</span></div>
    <div class="toc-item"><span>02 Lorem Ipsum</span><span>14</span></div>
  </div>
  <div class="abs toc-section" style="top:260px">
    <div class="toc-heading">Content Creation &amp; Distribution</div>
    <div class="toc-item"><span>01 Lorem Ipsum</span><span>15</span></div>
    <div class="toc-item"><span>02 Lorem Ipsum</span><span>17</span></div>
  </div>
  <div class="abs toc-section" style="top:299px">
    <div class="toc-heading">Goal Matrics</div>
    <div class="toc-item"><span>01 Lorem Ipsum</span><span>19</span></div>
    <div class="toc-item"><span>02 Lorem Ipsum</span><span>22</span></div>
  </div>
</section>

<!-- Letterhead -->
<section class="sheet letter">
  <div class="abs brand"><span class="mark-square" style="width:6px;height:6px"></span><span class="wordmark">valtoria</span></div>
  <div class="abs tagline">MARKETING &amp; CONSULTING</div>
  <div class="abs letter-sender">valtoria GmbH Lindhof &nbsp;|&nbsp; Ahornweg 14 &nbsp;|&nbsp; 52180 Feldstadt</div>
  <div class="abs letter-body">
    <p>Lorem ipsum dolor sit amet, consectetur adipiscing elit. Donec fringilla, dolor sit amet egestas fringilla, sem ante aliquet diam, quis vestibulum magna sem ac elit. Nam et consequat libero, sit amet gravida turpis. In congue lacinia massa. Integer semper malesuada odio ut dictum. Sed facilisis nisl dolor, sit amet porta velit euismod ut. Vivamus accumsan mauris id augue efficitur, et ullamcorper nibh dignissim.</p>
    <p>Fermentum neque cursus in. Nulla porta nulla purus, a luctus lectus molestie vel. Etiam cursus nisl et nisi tempus ultricies. Nullam vulputate turpis sit amet eleifend feugiat. Vestibulum congue iaculis risus eu pulvinar. Aliquam et felis non elit laoreet facilisis quis commodo ex. Suspendisse id sapien laoreet, malesuada ex ut, rhoncus risus. Donec ac ultricies nisi. Donec nec elit a sem gravida maximus a vitae mi.</p>
    <p>Vivamus pellentesque pharetra maximus. Nam quis nunc vitae dui vestibulum semper. Nulla at dictum turpis. Proin metus ligula, accumsan vel imperdiet sit amet, vestibulum id nulla. Quisque ornare, libero luctus condimentum malesuada, lectus diam feugiat risus, sed scelerisque justo nunc vel velit. Fermentum neque cursus in. Nulla porta nulla purus, a luctus lectus molestie vel. Etiam cursus nisl et nisi tempus ultricies. Nullam vulputate turpis sit amet eleifend feugiat.</p>
  </div>
  <div class="abs signature" role="img" aria-label="Handwritten signature of Baltrum"></div>
  <div class="abs letter-footer" style="left:25px">Geschäftsführer:<br>Baltrum<br><br>Amtsgericht Brennwald<br>HRB 4721</div>
  <div class="abs footer-rule" style="left:81px"></div>
  <div class="abs letter-footer" style="left:87px"><span style="color:var(--green)">Umsatzsteuer-ID</span><br>DE 900 417 263<br><span style="color:var(--green)">Nordhafen Bank Tessau</span><br>DE62 5003 0417 7788 2901 33<br>BIC: NOHBDE21TES</div>
  <div class="abs footer-rule" style="left:148px"></div>
  <div class="abs letter-footer" style="left:154px">
    <svg width="3" height="3" viewBox="0 0 10 10"><path d="M2 1l2 0 1 3-1.5 1a6 6 0 003 3L8 6.5l3 1v2C5 10 0 5 1 1z" fill="var(--green)"/></svg> +49 555 / 010 200<br>
    <svg width="3" height="3" viewBox="0 0 10 10"><rect x="1" y="2" width="8" height="6" fill="var(--green)"/></svg> +49 555 / 010 209<br>
    <svg width="3" height="3" viewBox="0 0 10 10"><circle cx="5" cy="5" r="4" fill="var(--green)"/></svg> info@valtoria.de
  </div>
  <svg class="abs" style="left:0;top:364px" width="269" height="16" viewBox="0 0 269 16">
    <polygon points="0,10 182,10 179,16 0,16" fill="var(--green)"/>
    <polygon points="187,1 269,1 269,16 181,16" fill="var(--navy)"/>
  </svg>
  <div class="abs url-tab" style="left:185px;top:367px;width:84px;font-size:7.5px">www.valtoria.de</div>
</section>

<!-- Envelope front -->
<svg class="abs" style="left:42px;top:935px" width="281" height="47" viewBox="0 0 281 47">
  <path d="M0 46 L14 4 Q15 0 20 0 L261 0 Q266 0 267 4 L281 46 Z" fill="var(--navy)"/>
</svg>
<section class="sheet envelope-front">
  <div class="abs brand"><span class="mark-square" style="width:5px;height:5px"></span><span class="wordmark">valtoria</span></div>
  <div class="abs tagline">MARKETING &amp; CONSULTING</div>
  <div class="abs address-window"></div>
  <svg class="abs" style="left:0;top:127px" width="281" height="14" viewBox="0 0 281 14">
    <polygon points="0,8 181,8 178,14 0,14" fill="var(--green)"/>
    <polygon points="186,0 281,0 281,14 180,14" fill="var(--navy)"/>
  </svg>
  <div class="abs url-tab" style="left:186px;top:128px;width:95px;font-size:7.5px">www.valtoria.de</div>
</section>

<!-- Business card front -->
<section class="sheet card-front">
  <div class="abs brand"><span class="mark-square" style="width:3.5px;height:3.5px"></span><span class="wordmark">valtoria</span></div>
  <div class="abs tagline">MARKETING &amp; CONSULTING</div>
  <div class="abs card-name">Baltrum</div>
  <div class="abs card-role">Marketing-und Vertriebsleitung</div>
  <div class="abs card-rule"></div>
  <div class="abs card-contact">0 555 0192<br>0 555 7316 48<br>baltrum@valtoria.de<br>www.valtoria.de</div>
  <div class="abs card-place">Standort Kirchgasse 9<br>37415 Rodau</div>
  <svg class="abs" style="left:0;top:60px" width="109" height="4" viewBox="0 0 109 4">
    <polygon points="0,1.5 77,1.5 76,4 0,4" fill="var(--green)"/>
    <polygon points="79,0 109,0 109,4 77,4" fill="var(--navy)"/>
  </svg>
</section>

<!-- Business card back -->
<section class="sheet card-back">
  <div class="abs wordmark">valtoria</div>
  <div class="abs card-back-url">www.valtoria.de</div>
</section>

<!-- Envelope back -->
<section class="sheet envelope-back">
  <svg class="abs" style="left:0;top:0" width="281" height="47" viewBox="0 0 281 47">
    <path d="M0 0 L281 0 L267 41 Q265 46 260 46 L21 46 Q16 46 14 41 Z" fill="var(--navy)"/>
  </svg>
</section>

</body>
</html>
```